【サイトマップ】
①TOP
②初めての方へ
③医師の紹介
④訪問診療について
⑤グループワーク
⑥漢方治療
⑦うつ病・双極性障害
⑧統合失調症
⑨認知症
⑩不安障害
⑪PMS・PMDD
⑫睡眠障害
⑬心身症
⑭発達障害
⑮お知らせ (一覧)
⑯お知らせ (詳細)
⑰ブログ (一覧)
⑱ブログ (詳細)
⑲お問い合せ・FAQ
⑳採用情報

【押していきたいメニュー】
⑥漢方治療
⑪PMS・PMDD

【デザインカラー】
ピンクなど淡い色合いにしていただければと存じます。

【デザインテイスト】
①清潔感
②優しい
③ナチュラル
※派手さやゴージャスなど敷居が高くなるイメージはNG×

【フォント】
游ゴシックか游明朝を使用してください。

【参考サイト(イメージに近いサイト)】
https://kaede-heart.example/

■参考にしたい部分
・優しさを感じるデザイン
・ユーザー目線を考えた構成(情報の分かりやすさ)

【ワイヤーフレーム】
http://hoshiweb.example.jp/client-check/tsubakiyume/wireframe/01
※構成は変えていただいて問題ございません。
またサイトマップと異なる情報が入っている箇所がございます。
サイトマップが最新情報となりますので、サイトマップの方に合わせてください。

【ロゴ】
http://hoshiweb.example.jp/client-check/tsubakiyume/rogo/10.A

【院の素材】
開業前なので、素材がございません。
清潔感があり、落ち着いている雰囲気を出し、
診療場所は完全個室の予定です。

【ブログ】
下記が開業に向け、書いているブログです。
もしデザイン作成に役立つ箇所がございましたら、
参考にしていただければ幸いです。
http://tsubaki487.example/

ピクセラ[ https://jp.pixela-stock.example/ ]で定期契約をしています。
クレジット購入のみのもの以外をご利用下さい。
また定期契約のものは弊社の負担となり、ランサー様に負担はありません。
カンプ画像を入れてください。
お世話になっております。
数多くのデザイン案を見てみたいので、
延長いたします。
皆様どうぞよろしくお願いいたします。

要望を的確に読み取って頂き、
一番近いデザインにしていただきました。

この度は当院のwebサイトTOPページを作成いただきまして誠にありがとうございます。
イメージしていたデザインよりもいいものができました。

また機会がございましたらぜひよろしくお願いいたします。

```html
<!DOCTYPE html>
<html lang="ja">
<head>
<meta charset="utf-8">
<title>つばきゆめクリニック</title>
<link href="https://fonts.googleapis.com/css2?family=M+PLUS+Rounded+1c:wght@400;500;700&family=Noto+Sans+JP:wght@400;500;700&family=Zen+Maru+Gothic:wght@500;700&display=swap" rel="stylesheet">
<style>
:root{
  --pink:#ef7fa3;
  --pink-deep:#e4668f;
  --pink-soft:#f9c9d8;
  --pink-pale:#fdeef3;
  --pink-band:#f6a9c1;
  --text:#5a5356;
  --muted:#8f878a;
  --line:#ead8de;
  --white:#fff;
  --green:#b9d99a;
}
*{box-sizing:border-box;margin:0;padding:0}
html,body{width:1200px;height:3948px;overflow:hidden}
body{font-family:"Noto Sans JP",sans-serif;color:var(--text);background:var(--white);font-size:14px;position:relative}
.heading-en{font-family:"M PLUS Rounded 1c",sans-serif;color:var(--pink);font-size:28px;font-weight:500;letter-spacing:.04em}
.heading-ja{font-size:12px;color:var(--muted);margin-top:2px}
.center{text-align:center}
.btn{display:inline-flex;align-items:center;justify-content:space-between;gap:14px;border:1px solid var(--pink);color:var(--pink);background:#fff;border-radius:30px;font-size:12px;padding:8px 20px;min-width:190px}
.btn::after{content:"›";font-size:16px;line-height:1}

/* top bar & header */
.topbar{height:22px;display:flex;justify-content:space-between;align-items:center;padding:0 14px;font-size:10px;color:var(--muted);border-bottom:1px solid var(--line)}
.topbar .links{display:flex;gap:14px;color:var(--pink)}
.header{height:100px;display:flex;align-items:center;padding:0 24px;justify-content:space-between}
.brand{display:flex;align-items:center;gap:12px}
.brand-mark{width:40px;height:40px;border-radius:50%;background:var(--pink-soft)}
.brand-name{font-family:"Zen Maru Gothic",sans-serif;font-size:22px;font-weight:700;color:var(--pink)}
.brand-sub{font-size:10px;color:var(--muted);display:block;margin-top:2px}
.gnav{display:flex;gap:22px;margin-left:auto;margin-right:28px}
.gnav a{display:flex;flex-direction:column;align-items:center;font-size:11px;color:var(--text);gap:6px}
.gnav .ico{width:42px;height:42px;border-radius:50%;background:var(--pink);display:flex;align-items:center;justify-content:center}
.tel-box{text-align:right}
.tel-box small{font-size:10px;color:var(--muted);display:block}
.tel-box .tel{display:inline-flex;align-items:center;gap:6px;background:var(--pink);color:#fff;border-radius:4px;padding:5px 12px;font-weight:700;font-size:17px;margin-top:4px}

/* hero */
.hero{height:360px;position:relative;background:radial-gradient(ellipse at 50% 45%,#fff 0,#fbe3ec 30%,#dbeccb 62%,#b8d897 100%);display:flex;align-items:center;justify-content:center}
.hero-frame{width:520px;height:300px;border-radius:50%;background:radial-gradient(ellipse,#f7a2bf 0,#f49ab8 55%,rgba(244,154,184,0) 72%);display:flex;align-items:center;justify-content:center}
.hero-copy{color:#fff;font-family:"Zen Maru Gothic",sans-serif;font-size:24px;font-weight:700;line-height:1.85;text-align:center;letter-spacing:.04em}

/* news */
.news{height:92px;display:flex;align-items:center;padding:0 180px;gap:40px}
.news .heading-en{font-size:24px}
.news-item{display:flex;gap:18px;font-size:12px;flex:1;border-bottom:1px solid var(--line);padding-bottom:10px}
.news-item time{color:var(--muted)}

/* concerns */
.concerns{height:560px;background:linear-gradient(#fdeef3 0,#fbe9f0 55%,#eaf2f8 75%,#d9ebc7 100%);padding-top:36px;position:relative}
.concerns-title{font-family:"Zen Maru Gothic",sans-serif;color:var(--pink);font-size:24px;font-weight:700;text-align:center}
.bubbles{display:flex;flex-wrap:wrap;justify-content:center;gap:26px 40px;width:840px;margin:40px auto 0}
.bubble{width:122px;height:122px;border-radius:50%;background:rgba(214,226,246,.9);display:flex;align-items:center;justify-content:center;text-align:center;font-size:13px;line-height:1.5;color:#5b6475;box-shadow:0 4px 10px rgba(150,160,190,.25)}
.concerns .btn-wrap{position:absolute;left:0;right:0;bottom:46px;text-align:center}
.concerns .btn{min-width:310px}

/* features */
.features{height:660px;background:var(--pink-pale);padding-top:34px}
.feature-row{display:flex;gap:24px;width:960px;margin:28px auto 0}
.feature-card{flex:1;background:#fff}
.feature-photo{height:150px}
.feature-card h3{font-family:"Zen Maru Gothic",sans-serif;color:var(--pink);font-size:17px;text-align:center;padding:16px 0 8px}
.feature-card p{font-size:11px;line-height:1.8;padding:0 20px 18px;color:var(--muted)}
.feature-wide{display:flex;gap:24px;width:960px;margin:24px auto 0}
.wide-card{flex:1;display:flex;background:#fff;height:130px}
.wide-card .feature-photo{width:180px;height:130px}
.wide-card div.body{padding:16px 18px}
.wide-card h3{font-family:"Zen Maru Gothic",sans-serif;color:var(--pink);font-size:15px;margin-bottom:8px}
.wide-card p{font-size:11px;line-height:1.8;color:var(--muted)}

/* symptoms */
.symptoms{height:280px;background:#fff;padding-top:28px;position:relative}
.symptoms::before{content:"";position:absolute;left:0;right:0;top:0;height:8px;background:var(--pink-band)}
.symptom-grid{display:grid;grid-template-columns:repeat(4,220px);gap:16px 26px;justify-content:center;margin-top:22px}
.symptom{height:62px;border:1px solid var(--pink-soft);border-radius:6px;display:flex;align-items:center;gap:14px;padding:0 14px;font-size:13px}
.symptom .dot{width:40px;height:40px;border-radius:50%;background:var(--pink-pale);border:2px solid var(--pink-soft);flex:none}
.symptom span{flex:1;text-align:center}

/* clinic info */
.clinic{height:380px;background:var(--pink-pale);display:flex;padding:44px 120px 0;gap:40px;position:relative}
.clinic::before{content:"";position:absolute;left:0;right:0;top:0;height:8px;background:var(--pink-band)}
.clinic-side{width:220px}
.clinic-side .btn{margin-top:14px;min-width:200px}
.clinic-main{flex:1}
.clinic-photos{display:flex;gap:10px;height:150px}
.clinic-photos div{flex:1}
table.hours{width:100%;border-collapse:collapse;margin-top:16px;font-size:11px;background:#fff}
.hours th{background:var(--pink);color:#fff;font-weight:500;padding:6px}
.hours td{border-bottom:1px solid var(--line);text-align:center;padding:7px;color:var(--pink)}
.hours td:first-child{color:var(--text)}
.clinic-note{font-size:10px;color:var(--muted);margin-top:8px;line-height:1.7}

/* access */
.access{height:380px;display:flex;padding:48px 120px 0;gap:40px}
.access-side{width:220px}
.access-side p{font-size:11px;line-height:1.9;margin-top:30px;color:var(--muted)}
.access-map{flex:1;display:flex;gap:10px;height:280px}
.access-map .feed{width:200px}
.access-map .map{flex:1}

/* blog */
.blog{height:380px;padding-top:20px}
.blog-grid{display:flex;gap:24px;width:960px;margin:24px auto 0}
.blog-card{flex:1}
.blog-card .photo{height:150px}
.blog-card h4{font-size:12px;font-weight:500;margin-top:10px;color:var(--pink)}
.blog-card time{font-size:10px;color:var(--muted)}
.blog .btn-wrap{text-align:center;margin-top:18px}

/* recruit */
.recruit{height:150px;display:flex;justify-content:center;align-items:center}
.recruit-banner{width:540px;height:96px;border:2px solid var(--pink-soft);display:flex;background:#fff}
.recruit-banner .photo{width:200px}
.recruit-banner .body{flex:1;display:flex;flex-direction:column;justify-content:center;align-items:center;gap:8px}
.recruit-banner strong{font-family:"Zen Maru Gothic",sans-serif;color:var(--pink);font-size:24px}
.recruit-banner .btn{min-width:160px;padding:4px 14px;font-size:10px}

/* footer */
.footer{height:312px;background:var(--pink);display:flex;align-items:center;justify-content:center;gap:60px;color:#fff}
.footer-brand{width:130px;height:130px;background:#fff;display:flex;flex-direction:column;align-items:center;justify-content:center;gap:8px;text-align:center}
.footer-brand .brand-mark{width:46px;height:46px}
.footer-brand span{font-family:"Zen Maru Gothic",sans-serif;color:var(--pink);font-size:12px;font-weight:700}
.footer-contact{text-align:center}
.footer-contact small{font-size:12px}
.footer-contact .tel{font-size:30px;font-weight:700;display:flex;align-items:center;gap:8px;margin:6px 0 14px}
.footer-contact .mail{display:inline-block;border:1px solid #fff;border-radius:30px;padding:8px 26px;font-size:12px;background:rgba(255,255,255,.15)}
.cal{background:#fff;color:var(--text);width:220px;font-size:10px;border-collapse:collapse}
.cal th{background:var(--pink-soft);padding:4px}
.cal td{text-align:center;padding:4px;color:var(--pink);border-bottom:1px solid var(--line)}
.cal-note{font-size:10px;margin-top:6px}
.sitemap{height:170px;padding:34px 140px 0;display:grid;grid-template-columns:repeat(10,1fr);gap:14px 10px;font-size:11px}
.sitemap a{color:var(--text)}
.copyright{height:54px;text-align:center;font-size:10px;color:var(--muted);border-top:1px solid var(--line);padding-top:16px}
a{text-decoration:none}
</style>
</head>
<body>

<div class="topbar">
  <span>自身の知識と経験を活かし心療内科・精神科の診療を行うクリニックです</span>
  <span class="links"><span>お問い合せ</span><span>アクセス</span></span>
</div>

<header class="header">
  <div class="brand">
    <span class="brand-mark"></span>
    <div><span class="brand-name">つばきゆめクリニック</span><span class="brand-sub">Tsubaki Yume Clinic</span></div>
  </div>
  <nav class="gnav">
    <a><span class="ico"><svg width="20" height="20" viewBox="0 0 20 20"><circle cx="10" cy="7" r="4" fill="#fff"/><path d="M3 18c1-4 4-6 7-6s6 2 7 6z" fill="#fff"/></svg></span>初めての方へ</a>
    <a><span class="ico"><svg width="20" height="20" viewBox="0 0 20 20"><rect x="4" y="3" width="12" height="14" rx="2" fill="none" stroke="#fff" stroke-width="2"/><path d="M7 8h6M7 12h6" stroke="#fff" stroke-width="2"/></svg></span>医師紹介</a>
    <a><span class="ico"><svg width="20" height="20" viewBox="0 0 20 20"><path d="M3 10l7-6 7 6v7H3z" fill="#fff"/></svg></span>訪問診療</a>
    <a><span class="ico"><svg width="20" height="20" viewBox="0 0 20 20"><path d="M4 4h12v9H8l-4 3z" fill="#fff"/></svg></span>お知らせ</a>
    <a><span class="ico"><svg width="20" height="20" viewBox="0 0 20 20"><circle cx="10" cy="10" r="7" fill="none" stroke="#fff" stroke-width="2"/><path d="M8 8a2 2 0 1 1 3 2v1" stroke="#fff" stroke-width="2" fill="none"/></svg></span>よくある質問</a>
  </nav>
  <div class="tel-box">
    <small>お問い合わせ受付 9:00〜18:00</small>
    <span class="tel"><svg width="14" height="14" viewBox="0 0 20 20"><path d="M5 2l3 4-2 2c1 3 3 5 6 6l2-2 4 3-2 3C9 18 2 11 2 4z" fill="#fff"/></svg>000-000-0000</span>
  </div>
</header>

<section class="hero" role="img" aria-label="柔らかな緑と光のイメージ写真、花のリースに囲まれたメッセージ">
  <div class="hero-frame">
    <p class="hero-copy">自身の知識と経験を活かし、<br>あなたに寄り添います。<br>ひとつだけ上を目指していきましょう。</p>
  </div>
</section>

<section class="news">
  <h2 class="heading-en">NEWS</h2>
  <div class="news-item"><time>2018.00.00</time><span>開院のお知らせ</span></div>
  <a class="btn">お知らせ一覧</a>
</section>

<section class="concerns">
  <h2 class="concerns-title">このようなお悩みありませんか？</h2>
  <div class="bubbles">
    <div class="bubble">気分が落ち込む</div>
    <div class="bubble">眠れない</div>
    <div class="bubble">不安感が<br>強い</div>
    <div class="bubble">集中力が<br>続かない</div>
    <div class="bubble">意欲がない</div>
    <div class="bubble">不安と<br>イライラが続く</div>
    <div class="bubble">動悸・息苦しい</div>
    <div class="bubble">物忘れ</div>
    <div class="bubble">対人関係が<br>うまくいかない</div>
  </div>
  <div class="btn-wrap"><a class="btn">お気軽にご相談ください</a></div>
</section>

<section class="features">
  <div class="center"><h2 class="heading-en">FEATURES</h2><p class="heading-ja">当院の特徴</p></div>
  <div class="feature-row">
    <article class="feature-card">
      <div class="feature-photo" role="img" aria-label="診察室で説明する医師の写真" style="background:linear-gradient(135deg,#eef1f4,#d9e1e8)"></div>
      <h3>患者様に寄り添った治療</h3>
      <p>お一人おひとりのお話を丁寧に伺い、生活に合わせた無理のない治療を一緒に考えていきます。</p>
    </article>
    <article class="feature-card">
      <div class="feature-photo" role="img" aria-label="女性医師の写真" style="background:linear-gradient(135deg,#f1f3f5,#dfe4ea)"></div>
      <h3>女性医師による診察</h3>
      <p>女性医師が診察を担当します。女性ならではのお悩みも安心してご相談ください。</p>
    </article>
    <article class="feature-card">
      <div class="feature-photo" role="img" aria-label="手で包んだハートのイメージ写真" style="background:linear-gradient(135deg,#fbe4e6,#f1c3c8)"></div>
      <h3>丁寧な対応</h3>
      <p>完全個室の落ち着いた空間で、時間をかけてゆっくりとお話を伺います。</p>
    </article>
  </div>
  <div class="feature-wide">
    <article class="wide-card">
      <div class="feature-photo" role="img" aria-label="漢方の生薬の写真" style="background:linear-gradient(135deg,#d9b48c,#a9754d)"></div>
      <div class="body"><h3>漢方治療にも力を入れています</h3><p>体質や症状に合わせた漢方薬を処方し、心と体の両面から整えていきます。</p></div>
    </article>
    <article class="wide-card">
      <div class="feature-photo" role="img" aria-label="お腹に手をあてる女性の写真" style="background:linear-gradient(135deg,#f6eee9,#e8d7cf)"></div>
      <div class="body"><h3>PMS・PMDDのお悩みの方へ</h3><p>月経前の心身の不調にお悩みの方へ、症状に合わせた治療をご提案します。</p></div>
    </article>
  </div>
</section>

<section class="symptoms">
  <div class="center"><h2 class="heading-en">SYMPTOMS</h2><p class="heading-ja">症状一覧</p></div>
  <div class="symptom-grid">
    <div class="symptom"><span class="dot"></span><span>うつ病・<br>双極性障害</span></div>
    <div class="symptom"><span class="dot"></span><span>統合失調症</span></div>
    <div class="symptom"><span class="dot"></span><span>認知症</span></div>
    <div class="symptom"><span class="dot"></span><span>不安障害</span></div>
    <div class="symptom"><span class="dot"></span><span>睡眠障害</span></div>
    <div class="symptom"><span class="dot"></span><span>PMS・PMDD</span></div>
    <div class="symptom"><span class="dot"></span><span>心身症</span></div>
    <div class="symptom"><span class="dot"></span><span>発達障害</span></div>
  </div>
</section>

<section class="clinic">
  <div class="clinic-side">
    <h2 class="heading-en">CLINIC INFO</h2><p class="heading-ja">医院案内</p>
    <div style="margin-top:18px">
      <a class="btn">初めての方へ</a>
      <a class="btn">医師の紹介</a>
      <a class="btn">訪問診療について</a>
    </div>
  </div>
  <div class="clinic-main">
    <div class="clinic-photos">
      <div role="img" aria-label="明るい院内の待合スペースの写真" style="background:linear-gradient(135deg,#f4f5f6,#dcdfe2)"></div>
      <div role="img" aria-label="受付カウンターの写真" style="background:linear-gradient(135deg,#eef0f1,#cfd6da)"></div>
    </div>
    <table class="hours">
      <tr><th>診療時間</th><th>月</th><th>火</th><th>水</th><th>木</th><th>金</th><th>土</th><th>日</th></tr>
      <tr><td>9:00〜12:00</td><td>●</td><td>●</td><td>●</td><td>ー</td><td>●</td><td>●</td><td>ー</td></tr>
      <tr><td>14:00〜18:00</td><td>●</td><td>●</td><td>●</td><td>ー</td><td>●</td><td>ー</td><td>ー</td></tr>
    </table>
    <p class="clinic-note">※ 初診の方はお電話にてご予約ください。<br>休診日：木・土曜午後・日曜・祝日</p>
  </div>
</section>

<section class="access">
  <div class="access-side">
    <h2 class="heading-en">ACCESS</h2><p class="heading-ja">アクセス</p>
    <p>〒000-0000<br>東京都星見区ゆめ町1丁目1番<br>ゆめビル2F<br>TEL：000-000-0000</p>
  </div>
  <div class="access-map">
    <div class="feed" role="img" aria-label="SNSの投稿タイムライン" style="background:#f7f7f8;border:1px solid var(--line)"></div>
    <div class="map" role="img" aria-label="クリニック周辺の地図" style="background:linear-gradient(135deg,#eef1ea,#e3e8de)"></div>
  </div>
</section>

<section class="blog">
  <div class="center"><h2 class="heading-en">BLOG</h2><p class="heading-ja">ブログ</p></div>
  <div class="blog-grid">
    <article class="blog-card"><div class="photo" role="img" aria-label="自然の中で過ごす人の写真" style="background:linear-gradient(135deg,#d5e6c6,#9fc38a)"></div><h4>ストレスの解消法</h4><time>2018.00.00</time></article>
    <article class="blog-card"><div class="photo" role="img" aria-label="打ち合わせをする人々の写真" style="background:linear-gradient(135deg,#e6e8ea,#b7bfc6)"></div><h4>カウンセリングについて</h4><time>2018.00.00</time></article>
    <article class="blog-card"><div class="photo" role="img" aria-label="淡い桜の花の写真" style="background:linear-gradient(135deg,#fbe2ea,#f3b8c9)"></div><h4>春の花便り</h4><time>2018.00.00</time></article>
  </div>
  <div class="btn-wrap"><a class="btn">ブログ一覧</a></div>
</section>

<section class="recruit">
  <div class="recruit-banner">
    <div class="photo" role="img" aria-label="医療スタッフの写真" style="background:linear-gradient(135deg,#eef3f6,#cbd8e0)"></div>
    <div class="body"><strong>スタッフ募集中!!</strong><a class="btn">採用情報はこちら</a></div>
  </div>
</section>

<footer class="footer">
  <div class="footer-brand"><span class="brand-mark"></span><span>つばきゆめ<br>クリニック</span></div>
  <div class="footer-contact">
    <small>お問い合わせ</small>
    <div class="tel"><svg width="26" height="26" viewBox="0 0 20 20"><path d="M5 2l3 4-2 2c1 3 3 5 6 6l2-2 4 3-2 3C9 18 2 11 2 4z" fill="#fff"/></svg>000-000-0000</div>
    <a class="mail">メールでのお問い合わせ ›</a>
  </div>
  <div>
    <table class="cal">
      <tr><th>時間</th><th>月</th><th>火</th><th>水</th><th>木</th><th>金</th><th>土</th><th>日</th></tr>
      <tr><td style="color:var(--text)">午前</td><td>●</td><td>●</td><td>●</td><td>ー</td><td>●</td><td>●</td><td>ー</td></tr>
      <tr><td style="color:var(--text)">午後</td><td>●</td><td>●</td><td>●</td><td>ー</td><td>●</td><td>ー</td><td>ー</td></tr>
    </table>
    <p class="cal-note">休診日：木・土曜午後・日曜・祝日</p>
  </div>
</footer>

<nav class="sitemap">
  <a>TOP</a><a>初めての方へ</a><a>医師の紹介</a><a>訪問診療</a><a>グループワーク</a><a>漢方治療</a><a>よくある質問</a><a>お知らせ</a><a>ブログ</a><a>採用情報</a>
  <a>うつ病・双極性</a><a>統合失調症</a><a>認知症</a><a>不安障害</a><a>PMS・PMDD</a><a>睡眠障害</a><a>心身症</a><a>発達障害</a><a>お問い合せ</a><a>アクセス</a>
</nav>
<div class="copyright">Copyright © Tsubaki Yume Clinic All Rights Reserved.</div>

</body>
</html>
```